Envelope Design Project

I will need two envelopes to be designed:-

DL size
C4 size

Please see uploaded documents for Design specs:

1) Design specs provided by printer (doc called DL Envelope Specs)
2) Design specs to comply with Kestrel Mailways requirements (doc called Kestrel Mailways Envelope Design Requirements)

Please adhere to the above for final design. Many thanks.

Target Market(s)

Real Estate Agents, Strata Managers, Builders, Architects, Business Owners

Industry/Entity Type

Printer

Requirements
Must have
• In top left corner
- Logo
- Return address - Suite 5, 19 Wattlebark Rd, Marrowick, NSW 2417

```html
<!DOCTYPE html>
<html lang="en">
<head>
<meta charset="utf-8">
<title>Tarnell Asbestos &amp; Safety – Envelopes</title>
<link rel="stylesheet" href="https://fonts.googleapis.com/css2?family=Didact+Gothic&display=swap">
<style>
  :root {
    --backdrop: #ededed;
    --paper: #e6e6e6;
    --navy: #2a2a40;
    --lime: #9dc13b;
    --address-grey: #555555;
  }
  html, body {
    margin: 0;
    padding: 0;
    width: 1200px;
    height: 1000px;
    overflow: hidden;
    background: var(--backdrop);
    font-family: "Didact Gothic", "Century Gothic", sans-serif;
  }
  .canvas {
    position: relative;
    width: 1200px;
    height: 1000px;
  }
  .envelope {
    position: absolute;
    background: var(--paper);
  }
  .envelope--dl {
    left: 85px;
    top: 67px;
    width: 530px;
    height: 263px;
  }
  .envelope--c4 {
    left: 345px;
    top: 405px;
    width: 757px;
    height: 535px;
  }

  .sender {
    position: absolute;
    display: flex;
    flex-direction: column;
  }
  .envelope--dl .sender { left: 37px; top: 40px; gap: 12px; }
  .envelope--c4 .sender { left: 62px; top: 58px; gap: 20px; }

  .brand {
    display: flex;
    align-items: center;
    color: var(--navy);
  }
  .brand__square {
    background: var(--navy);
    border-radius: 4px;
    flex: none;
  }
  .brand__name {
    line-height: 1.1;
    white-space: nowrap;
    text-transform: uppercase;
    letter-spacing: 0.02em;
  }
  .envelope--dl .brand { gap: 8px; }
  .envelope--dl .brand__square { width: 28px; height: 28px; }
  .envelope--dl .brand__name { font-size: 13px; }

  .envelope--c4 .brand { gap: 14px; }
  .envelope--c4 .brand__square { width: 55px; height: 55px; border-radius: 7px; }
  .envelope--c4 .brand__name { font-size: 24px; }

  .return-address {
    margin: 0;
    font-style: normal;
    color: var(--address-grey);
  }
  .envelope--dl .return-address { font-size: 8px; line-height: 10px; }
  .envelope--c4 .return-address { font-size: 11px; line-height: 14px; }

  .accent-bar {
    position: absolute;
    right: 0;
    background: var(--lime);
  }
  .envelope--dl .accent-bar { top: 202px; width: 11px; height: 35px; }
  .envelope--c4 .accent-bar { top: 437px; width: 14px; height: 51px; }
</style>
</head>
<body>
<main class="canvas">
  <section class="envelope envelope--dl" aria-label="DL envelope">
    <div class="sender">
      <div class="brand">
        <span class="brand__square"></span>
        <span class="brand__name">Tarnell<br>Asbestos &amp; Safety</span>
      </div>
      <address class="return-address">Suite 5, 19 Wattlebark Rd<br>Marrowick, NSW 2417</address>
    </div>
    <span class="accent-bar"></span>
  </section>

  <section class="envelope envelope--c4" aria-label="C4 envelope">
    <div class="sender">
      <div class="brand">
        <span class="brand__square"></span>
        <span class="brand__name">Tarnell<br>Asbestos &amp; Safety</span>
      </div>
      <address class="return-address">Suite 5, 19 Wattlebark Rd<br>Marrowick, NSW 2417</address>
    </div>
    <span class="accent-bar"></span>
  </section>
</main>
</body>
</html>
```